Photoshop Templates for Instagram, x 2

A Square template to reuse that is on brand.

It will involve an image and text of between 3 and 10 words.
I would like 2 separate contrasting images to use interchangeably

In the files I have added some of the images that I have been using, as well as the home page of my website that is currently being developed.

The on brand would be very recognisable with the website.

Requirements
Must have
• Must be similar in feel to the home page.

Must be simple to to change image and and text in the template

I would like 2 designs. Both similar, but contrasting

The square images show the look that I have been using (created by myself, so I'm sure these can be massively improved upon)

```html
<!DOCTYPE html>
<html lang="en">
<head>
<meta charset="utf-8">
<title>Peakmind – Square Post Templates</title>
<link rel="stylesheet" href="https://fonts.googleapis.com/css2?family=Montserrat:wght@500;700;800&display=swap">
<style>
  :root {
    --page: #ffffff;
    --brand-blue: #0a8bd4;
    --brand-blue-deep: #0569a8;
    --navy-night: #02121e;
    --ink-dark: #121417;
    --stripe-dark: #16181c;
    --photo-mono-light: #8f8f8f;
    --photo-mono-dark: #2b2b2b;
    --photo-tint-light: #7d92a8;
    --photo-tint-dark: #34475e;
    --text-light: #ffffff;
  }
  * { margin: 0; padding: 0; box-sizing: border-box; }
  html, body {
    width: 1200px;
    height: 614px;
    overflow: hidden;
    background: var(--page);
  }
  .canvas {
    position: relative;
    width: 1200px;
    height: 614px;
  }
  .post {
    position: absolute;
    top: 24px;
    width: 567px;
    height: 567px;
    overflow: hidden;
  }
  .post--blue { left: 21px; }
  .post--dark { left: 612px; }
  .post svg {
    display: block;
    width: 567px;
    height: 567px;
  }
  .headline,
  .player-name,
  .brand-name {
    font-family: "Montserrat", sans-serif;
    fill: var(--text-light);
  }
  .headline { font-weight: 800; font-size: 49px; }
  .headline--accent { font-size: 67px; }
  .player-name { font-weight: 500; font-size: 19px; letter-spacing: 1px; }
  .brand-name { font-weight: 800; font-size: 13.5px; }
</style>
</head>
<body>
<main class="canvas">

  <!-- Blue variant -->
  <section class="post post--blue">
    <svg viewBox="0 0 567 567" aria-labelledby="blue-title">
      <title id="blue-title">Blue square post template</title>
      <defs>
        <linearGradient id="blue-ground" x1="0" y1="0" x2="0" y2="1">
          <stop offset="0" stop-color="var(--brand-blue)"/>
          <stop offset="0.45" stop-color="var(--brand-blue-deep)"/>
          <stop offset="0.8" stop-color="var(--navy-night)"/>
        </linearGradient>
        <linearGradient id="blue-corner" x1="1" y1="0" x2="0" y2="1">
          <stop offset="0" stop-color="var(--brand-blue)"/>
          <stop offset="1" stop-color="var(--navy-night)"/>
        </linearGradient>
        <radialGradient id="mono-photo" cx="0.6" cy="0.35" r="0.75">
          <stop offset="0" stop-color="var(--photo-mono-light)"/>
          <stop offset="1" stop-color="var(--photo-mono-dark)"/>
        </radialGradient>
      </defs>

      <rect class="post-ground" width="567" height="567" fill="url(#blue-ground)"/>

      <g class="photo-window" role="img" aria-label="Black and white action photo of a footballer in a striped kit">
        <polygon points="85,107 106,131 271,0 220,0" fill="url(#mono-photo)"/>
        <polygon points="80,210 140,279 247,555 567,265 567,0 300,0" fill="url(#mono-photo)"/>
      </g>

      <g class="accent-stripes" stroke="var(--brand-blue)" stroke-width="13">
        <line x1="125" y1="285" x2="470" y2="-10"/>
        <line x1="375" y1="525" x2="580" y2="335"/>
      </g>
      <polygon class="corner-band" points="567,392 567,567 290,567 420,480" fill="url(#blue-corner)"/>

      <g class="brand">
        <circle cx="26" cy="27" r="12" fill="none" stroke="var(--text-light)" stroke-width="2.4"/>
        <text class="brand-name" x="42" y="32">PEAKMIND</text>
      </g>

      <g class="headline-block">
        <text class="headline" x="21" y="315" textLength="237" lengthAdjust="spacingAndGlyphs">A SQUARE</text>
        <text class="headline" x="21" y="373" textLength="237" lengthAdjust="spacingAndGlyphs">TEMPLATE</text>
        <text class="headline" x="21" y="427" textLength="237" lengthAdjust="spacingAndGlyphs">TO REUSE</text>
        <text class="headline" x="21" y="480" textLength="237" lengthAdjust="spacingAndGlyphs">THAT IS ON</text>
        <text class="headline headline--accent" x="20" y="546" textLength="238" lengthAdjust="spacingAndGlyphs">BRAND</text>
      </g>
      <text class="player-name" x="536" y="546" text-anchor="end">MARCO VALENTE</text>
    </svg>
  </section>

  <!-- Dark variant -->
  <section class="post post--dark">
    <svg viewBox="0 0 567 567" aria-labelledby="dark-title">
      <title id="dark-title">Dark square post template</title>
      <defs>
        <radialGradient id="tint-photo" cx="0.6" cy="0.35" r="0.75">
          <stop offset="0" stop-color="var(--photo-tint-light)"/>
          <stop offset="1" stop-color="var(--photo-tint-dark)"/>
        </radialGradient>
      </defs>

      <rect class="post-ground" width="567" height="567" fill="var(--ink-dark)"/>

      <g class="photo-window" role="img" aria-label="Blue-tinted action photo of a footballer in a striped kit">
        <polygon points="85,107 106,131 271,0 220,0" fill="url(#tint-photo)"/>
        <polygon points="80,210 140,279 247,555 567,265 567,0 300,0" fill="url(#tint-photo)"/>
      </g>

      <g class="accent-stripes" stroke="var(--stripe-dark)" stroke-width="13">
        <line x1="125" y1="285" x2="470" y2="-10"/>
        <line x1="375" y1="525" x2="580" y2="335"/>
      </g>
      <polygon class="corner-band" points="567,392 567,567 290,567 420,480" fill="var(--ink-dark)"/>

      <g class="brand">
        <circle cx="26" cy="27" r="12" fill="none" stroke="var(--text-light)" stroke-width="2.4"/>
        <text class="brand-name" x="42" y="32">PEAKMIND</text>
      </g>

      <g class="headline-block">
        <text class="headline" x="21" y="315" textLength="237" lengthAdjust="spacingAndGlyphs">A SQUARE</text>
        <text class="headline" x="21" y="373" textLength="237" lengthAdjust="spacingAndGlyphs">TEMPLATE</text>
        <text class="headline" x="21" y="427" textLength="237" lengthAdjust="spacingAndGlyphs">TO REUSE</text>
        <text class="headline" x="21" y="480" textLength="237" lengthAdjust="spacingAndGlyphs">THAT IS ON</text>
        <text class="headline headline--accent" x="20" y="546" textLength="238" lengthAdjust="spacingAndGlyphs">BRAND</text>
      </g>
      <text class="player-name" x="536" y="546" text-anchor="end">MARCO VALENTE</text>
    </svg>
  </section>

</main>
</body>
</html>
```